Banner Ad and Digital Ad design for tradeshow

I need two graphics designed (can be same/similar design just different dimensions. We are an engineering firm practicing in the solid waste industry. We are a conference sponsor and need two graphics.
(1) Banner Ad - 300x250 - gif, png, jped, html, or other. Imagery with our mantra - Driven by purpose. Guided by stewardship. Striving for excellence.
(2) Digital Ad (static) - 1920x1080 hi-res jpg or png.

Target Market(s)

Solid Waste Management Industry (Environmental)

Industry/Entity Type

Environmental

Requirements
Must have
• Quality Aesthetic
Nice to have
• Great Imagery + our mantra

```html
<!DOCTYPE html>
<html lang="en">
<head>
<meta charset="utf-8">
<title>Vantor Engineering – Tradeshow Ads</title>
<link href="https://fonts.googleapis.com/css2?family=Josefin+Sans:wght@600;700&family=Michroma&display=swap" rel="stylesheet">
<style>
  :root {
    --canvas: #ffffff;
    --ink-dark: #1b1c1c;
    --ink-light: #ffffff;
    --label-green: #7d9070;
    --label-grey: #2c2d2d;
    --sky-top: #5d6061;
    --sky-mid: #c9cccc;
    --ground: #0d0d0d;
    --brand-green: #5f8a4e;
    --brand-light: #d9dcdc;
    --site-dark: #0f1110;
    --site-soil: #7a6549;
    --site-teal: #2c3c45;
    --site-forest: #3d4a26;
  }
  * { margin: 0; padding: 0; box-sizing: border-box; }
  html, body { width: 1200px; height: 535px; overflow: hidden; background: var(--canvas); }
  .canvas { position: relative; width: 1200px; height: 535px; }

  .ad { position: absolute; overflow: hidden; }
  .ad-banner { left: 42px; top: 37px; width: 283px; height: 235px; }
  .ad-digital { left: 346px; top: 38px; width: 813px; height: 458px; }

  .photo { position: absolute; inset: 0; }
  .ad-banner .photo {
    background:
      linear-gradient(180deg, transparent 0 72%, var(--ground) 72% 100%),
      linear-gradient(180deg, var(--sky-top) 0%, var(--sky-mid) 40%, #e4e6e6 62%, #b9bcbc 72%);
  }
  .ad-digital .photo {
    background:
      linear-gradient(90deg, var(--site-dark) 0%, rgba(15,17,16,0.85) 25%, rgba(15,17,16,0) 65%),
      radial-gradient(ellipse at 55% 45%, var(--site-soil) 0%, transparent 45%),
      linear-gradient(180deg, var(--site-forest) 0%, #2a3224 18%, var(--site-teal) 55%, #151a1c 100%);
  }

  .mantra { position: absolute; }
  .label { display: block; font-family: "Michroma", sans-serif; line-height: 1; text-transform: uppercase; white-space: nowrap; }
  .word { display: block; font-family: "Josefin Sans", sans-serif; font-weight: 700; line-height: 1; text-transform: uppercase; white-space: nowrap; }

  .ad-banner .mantra { left: 75px; top: 50px; color: var(--ink-dark); }
  .ad-banner .label { font-size: 5.5px; letter-spacing: 0.6px; color: var(--label-grey); margin-bottom: 1px; }
  .ad-banner .word { font-size: 19px; letter-spacing: 0.9px; margin-bottom: 5px; }

  .ad-digital .mantra { left: 62px; top: 104px; color: var(--ink-light); }
  .ad-digital .label { font-size: 16px; letter-spacing: 2.4px; color: var(--label-green); }
  .ad-digital .word { font-size: 53px; letter-spacing: 4.4px; margin-top: 4px; margin-bottom: 20px; }

  .brand { position: absolute; display: flex; align-items: center; }
  .brand-square { flex: none; }
  .brand-name {
    display: flex; flex-direction: column;
    font-family: "Josefin Sans", sans-serif; font-weight: 600;
    line-height: 1; text-transform: uppercase; white-space: nowrap;
  }

  .ad-banner .brand { left: 76px; top: 194px; gap: 5px; }
  .ad-banner .brand-square { width: 17px; height: 17px; background: var(--brand-green); }
  .ad-banner .brand-name { color: var(--brand-light); }
  .ad-banner .brand-primary { font-size: 11px; letter-spacing: 1.2px; }
  .ad-banner .brand-secondary { font-size: 4.6px; letter-spacing: 2.1px; margin-top: 2px; }

  .ad-digital .brand { left: 577px; top: 364px; gap: 10px; }
  .ad-digital .brand-square { width: 38px; height: 38px; background: var(--ink-light); }
  .ad-digital .brand-name { color: var(--ink-light); }
  .ad-digital .brand-primary { font-size: 22px; letter-spacing: 3.6px; }
  .ad-digital .brand-secondary { font-size: 9.5px; letter-spacing: 4.8px; margin-top: 4px; }
</style>
</head>
<body>
<main class="canvas">

  <section class="ad ad-banner" aria-label="Banner ad 300 by 250">
    <div class="photo" role="img" aria-label="Grey cloudy sky over a dark horizon with silhouetted excavators on a landfill"></div>
    <div class="mantra">
      <span class="label">Driven by</span>
      <span class="word">Purpose.</span>
      <span class="label">Guided by</span>
      <span class="word">Stewardship.</span>
      <span class="label">Striving for</span>
      <span class="word">Excellence.</span>
    </div>
    <div class="brand">
      <span class="brand-square"></span>
      <span class="brand-name">
        <span class="brand-primary">Vantor</span>
        <span class="brand-secondary">Engineering</span>
      </span>
    </div>
  </section>

  <section class="ad ad-digital" aria-label="Digital ad 1920 by 1080">
    <div class="photo" role="img" aria-label="Aerial view at dusk of a terraced landfill site with haul roads, soil stockpiles and surrounding forest"></div>
    <div class="mantra">
      <span class="label">Driven by</span>
      <span class="word">Purpose</span>
      <span class="label">Guided by</span>
      <span class="word">Stewardship</span>
      <span class="label">Striving for</span>
      <span class="word">Excellence</span>
    </div>
    <div class="brand">
      <span class="brand-square"></span>
      <span class="brand-name">
        <span class="brand-primary">Vantor</span>
        <span class="brand-secondary">Engineering</span>
      </span>
    </div>
  </section>

</main>
</body>
</html>
```